harvest Soon Book Cover Design for real estate investment book

I am looking for a Book Cover design for my new book. I would like designs for a hardcover, softcover and Lumora book.

The book deals with real estate and mortgage investments. Looking for a clean, bright simple design. Want to cover to be White with big RED letters. See "Dancing past Noon" book for an example ... see attached.

Target Market(s)

Affluent people with money looking for investment solutions.

Industry/Entity Type

Financial Service

Font styles to use
Serif

Requirements
Must have
• Bright clean design that will be appealing to affluent people.
• Title: harvest SOON
• Subtitle: A quiet method for thriving through land holdings
• subsubtitle: Secrets the Bank Teller Keeps Hidden From Clients...
• Author: Ned Falconby
• My Picture on the inside cover or on the back cover
• Book Description, Author description
Nice to have
• Focus on the Front cover look and feel first. Then we can look at the inside flaps and back cover. I will need to send you text. This is for the full cover. Front. Back. Spine. Inside flaps fro hardcover.

```html
<!DOCTYPE html>
<html lang="en">
<head>
<meta charset="utf-8">
<title>harvest Soon — Ned Falconby</title>
<link rel="stylesheet" href="https://fonts.googleapis.com/css2?family=Bebas+Neue&family=Libre+Bodoni:wght@500;600&display=swap">
<style>
  :root {
    --paper: #ffffff;
    --title-red: #8e1410;
    --ink: #111111;
  }
  html, body {
    margin: 0;
    padding: 0;
    overflow: hidden;
    background: var(--paper);
  }
  .cover {
    position: relative;
    width: 800px;
    height: 1200px;
    background: var(--paper);
    overflow: hidden;
  }
  .cover-art {
    position: absolute;
    inset: 0;
  }
  .display {
    font-family: "Bebas Neue", "Oswald", sans-serif;
    fill: var(--title-red);
  }
  .author-name {
    font-family: "Bebas Neue", "Oswald", sans-serif;
    fill: var(--ink);
  }
  .subtitle {
    position: absolute;
    left: 0;
    right: 0;
    top: 398px;
    margin: 0;
    text-align: center;
    font-family: "Libre Bodoni", "Bodoni Moda", serif;
    font-weight: 600;
    font-size: 25px;
    line-height: 38px;
    letter-spacing: -0.01em;
    color: var(--ink);
    text-transform: uppercase;
  }
  .tagline {
    position: absolute;
    left: 0;
    right: 0;
    top: 938px;
    margin: 0;
    text-align: center;
    font-family: "Libre Bodoni", "Bodoni Moda", serif;
    font-weight: 500;
    font-size: 21px;
    line-height: 36px;
    letter-spacing: 0.36em;
    color: var(--ink);
    text-transform: uppercase;
  }
</style>
</head>
<body>
  <main class="cover">
    <svg class="cover-art" width="800" height="1200" viewBox="0 0 800 1200" xmlns="http://www.w3.org/2000/svg">
      <title>harvest SOON by Ned Falconby</title>
      <text class="display title-top" x="42" y="360" font-size="451" textLength="716" lengthAdjust="spacingAndGlyphs">HARVEST</text>
      <g class="display title-bottom" font-size="546">
        <text x="42" y="894" textLength="120" lengthAdjust="spacingAndGlyphs">S</text>
        <text x="241" y="894" textLength="120" lengthAdjust="spacingAndGlyphs">O</text>
        <text x="439" y="894" textLength="120" lengthAdjust="spacingAndGlyphs">O</text>
        <text x="638" y="894" textLength="120" lengthAdjust="spacingAndGlyphs">N</text>
      </g>
      <text class="author-name" x="54" y="1152" font-size="160" textLength="690" lengthAdjust="spacingAndGlyphs">NED FALCONBY</text>
    </svg>

    <p class="subtitle">A quiet method for thriving<br>through land holdings</p>
    <p class="tagline">Secrets the Bank Teller<br>Keeps Hidden From Clients</p>
  </main>
</body>
</html>
```